Lanternfold Cybersecurity Web Site Project

Lanternfold Cybersecurity is an MSP provider that is a full-service IT delivery organization focused on service deliver and information security.

We are looking for CREATIVE and UNIQUE website design that lays out the initial landing page and content page for us to continue developing for our organization. We have attached a .zip of our logo and images stock for you to incorporate into the site.

We are a Cybersecurity / MSP focused on providing a full-service outsourced IT Services to organizations that also have information cybersecurity compliance requirements such as HIPAA, PCI-DSS,
NYS DFS 23 NYCRR 500.

Systems / Applications Solutions:
On-Premises and Cloud Solutions
IT Services / Help Desk
User and System Issue Resolution
Office365 Administration
Azure / Cloud Virtualization
Windows / Linux Server Administration

We are looking for two (2) .psd design files for the landing page and content page based on the logo stock art provided and all files / artwork created by the designer at project completion.

Please be creative and make this site stand out from all others. We are well aware of template sites like Pixel Orchard and others like it, so please we are not looking for a template we could download ourselves.

Target Market(s)

Demographic: Law Firms, Legal Services, Small - Medium Doctor offices, Medical services companies, Finance, Mortgage, Securities.

Businesses looking to outsource their IT departments.
Move to a full cloud business solution.
Require cybersecurity compliance such as HIPAA, PCI-DSS or DFS 23 NYCRR 500.

Industry/Entity Type

Information Technology

Number of Pages Required

2 page

Requirements
Must have
• We have included stock art for logo's, banners, headers, footers, please use that graphic stock for the site.

We operate in the Managed Service Provider (MSP) and Cybersecurity space
Should not have
• Themes we can get from any of the theme sites out there. We are looking for something completely new and unique.

```html
<!DOCTYPE html>
<html lang="en">
<head>
<meta charset="utf-8">
<title>Lanternfold Cybersecurity</title>
<link href="https://fonts.googleapis.com/css2?family=Orbitron:wght@700;800;900&family=Montserrat:wght@400;500;600;700&display=swap" rel="stylesheet">
<style>
:root{
  --red:#c4161c;
  --red-deep:#8e0d10;
  --navy:#1b1f4b;
  --ink:#111;
  --grey-band:#ececec;
  --dark:#222;
  --black:#050505;
  --copy-bar:#1c1c1c;
  --text:#333;
}
*{margin:0;padding:0;box-sizing:border-box}
html,body{width:1200px;height:3369px;overflow:hidden;background:#fff}
body{font-family:'Montserrat',sans-serif;color:var(--text);position:relative}
.display{font-family:'Orbitron',sans-serif;font-weight:900;letter-spacing:1px}
section,header,footer{position:absolute;left:0;width:1200px;overflow:hidden}
.abs{position:absolute}

/* header */
.site-header{top:0;height:118px}
.brand{position:absolute;left:59px;top:30px;display:flex;align-items:center;gap:10px;font-weight:700;font-size:17px;color:var(--navy)}
.brand-mark{width:30px;height:30px;background:var(--red)}
.nav{position:absolute;right:60px;top:31px;display:flex;align-items:center;gap:30px;font-size:13px}
.nav a{text-decoration:none;color:#222;text-transform:uppercase}
.nav a.active{color:var(--red);font-weight:700}
.nav .pill{border:1.5px solid #222;border-radius:16px;padding:6px 20px;font-weight:600}

/* hero */
.hero{top:118px;height:543px}
.hero h1{position:absolute;left:59px;top:160px;font-size:60px;color:var(--ink)}
.hero p{position:absolute;left:59px;top:240px;width:520px;font-size:13.5px;line-height:20px;color:#333}
.btn-dark{position:absolute;left:63px;top:339px;width:154px;height:38px;background:#111;color:#fff;font-size:13px;font-weight:500;display:flex;align-items:center;justify-content:center}
.hero-device{position:absolute;left:722px;top:32px;width:520px;height:398px;background:#111;border-radius:18px 0 0 0}
.hero-screen{position:absolute;left:14px;top:22px;right:0;bottom:22px;background:linear-gradient(135deg,#3a0406,#b5141a 50%,#4a0507)}
.hero-base{position:absolute;left:722px;top:440px;width:500px;height:18px;background:linear-gradient(#e6e6e6,#a9a9a9);border-radius:0 0 0 14px}

/* partner band */
.partners{top:661px;height:89px;background:var(--black);display:flex;align-items:center;justify-content:space-between;padding:0 59px}
.partner{display:flex;align-items:center;gap:8px;color:#fff;font-size:21px;font-weight:600}
.partner i{width:22px;height:22px;border:2px solid #fff;border-radius:50%;display:block}

/* about */
.about{top:750px;height:467px;background:var(--grey-band)}
.eyebrow{font-size:19px;color:#333;text-transform:uppercase;font-weight:400}
.section-title{font-size:38px;color:var(--navy)}
.about .eyebrow{position:absolute;left:59px;top:90px}
.about .section-title{position:absolute;left:59px;top:120px}
.about p{position:absolute;left:59px;top:193px;width:530px;font-size:15px;line-height:30px}
.learn{position:absolute;left:59px;top:343px;font-size:14px;font-weight:700;color:var(--navy);display:flex;align-items:center;gap:8px}
.about-device{position:absolute;left:780px;top:101px;width:343px;height:226px;background:#111;border-radius:10px}
.about-screen{position:absolute;left:10px;top:14px;right:10px;bottom:10px;background:linear-gradient(135deg,#6b4a35,#3a3a3f 50%,#8a6a50)}
.about-base{position:absolute;left:739px;top:327px;width:426px;height:14px;background:linear-gradient(#eee,#9d9d9d);border-radius:0 0 8px 8px}

/* services */
.services{top:1217px;height:645px}
.services .eyebrow{position:absolute;top:90px;width:100%;text-align:center}
.services .section-title{position:absolute;top:118px;width:100%;text-align:center;font-size:40px}
.card{position:absolute;top:204px;width:249px;height:334px;background:linear-gradient(160deg,#c01a1f,#8c0a0d);box-shadow:0 6px 14px rgba(0,0,0,.3);color:#fff}
.card small{position:absolute;left:19px;top:30px;font-size:12px;text-transform:uppercase}
.card h3{position:absolute;left:19px;top:44px;font-size:28px}
.card p{position:absolute;left:19px;top:204px;width:220px;font-size:13px;font-weight:500;line-height:20px}
.card .btn{position:absolute;left:19px;top:266px;width:147px;height:32px;background:#fff;color:var(--navy);font-family:'Orbitron',sans-serif;font-weight:800;font-size:12px;display:flex;align-items:center;justify-content:center}

/* works */
.works{top:1862px;height:367px;background:var(--dark)}
.work{position:absolute;top:29px;width:285px;height:163px}
.work .frame{position:absolute;left:28px;top:0;width:229px;height:153px;background:#0e0e0e;border-radius:6px 6px 0 0}
.work .screen{position:absolute;left:6px;top:6px;right:6px;bottom:6px}
.work .base{position:absolute;left:0;bottom:0;width:285px;height:10px;background:linear-gradient(#ddd,#999);border-radius:0 0 5px 5px}
.works h2{position:absolute;top:233px;width:100%;text-align:center;font-size:38px;color:#fff}
.btn-outline{position:absolute;left:522px;top:284px;width:155px;height:37px;border:1px solid #fff;color:#fff;font-size:13px;font-weight:600;display:flex;align-items:center;justify-content:center}

/* testimonials */
.clients{top:2229px;height:573px}
.clients .eyebrow{position:absolute;top:56px;width:100%;text-align:center}
.clients .section-title{position:absolute;top:80px;width:100%;text-align:center;font-size:40px}
.quote{position:absolute;top:225px;width:64px;height:50px}
.avatar{position:absolute;top:182px;width:78px;height:78px;border-radius:50%}
.quote-text{position:absolute;top:276px;width:300px;font-size:15px;line-height:30px;color:#222}
.client-name{position:absolute;top:411px;font-size:15px;font-weight:700;color:var(--navy)}
.client-since{position:absolute;top:436px;font-size:12px;color:#555;text-transform:uppercase}

/* cta */
.cta{top:2802px;height:375px;background:linear-gradient(160deg,#2a0304 0%,#6b0709 50%,#8b0b0d 100%)}
.cta h2{position:absolute;left:59px;top:115px;font-size:38px;color:#fff}
.field{position:absolute;top:184px;width:368px;height:45px;border-radius:23px;background:#fff;font-size:14px;color:#999;padding:0 20px;display:flex;align-items:center}
.cta-btn{position:absolute;left:59px;top:253px;width:183px;height:44px;border:1.5px solid #fff;border-radius:22px;color:#fff;font-size:20px;font-weight:600;display:flex;align-items:center;justify-content:center}
.cta-devices{position:absolute;left:920px;top:60px;width:330px;height:290px;border-radius:26px;background:linear-gradient(135deg,#f0a3c0,#8a5ad8 55%,#2a2a3a);transform:rotate(-28deg);border:6px solid #1a1a1a}

/* footer */
.site-footer{top:3177px;height:136px;background:var(--black)}
.site-footer .brand{top:53px;color:#fff}
.site-footer .nav{top:52px}
.site-footer .nav a{color:#fff}
.site-footer .nav a.active{color:#fff}
.site-footer .nav .pill{border-color:#fff}
.copyright{top:3313px;height:56px;background:var(--copy-bar);color:#ddd;font-size:13px;padding:20px 59px 0}
</style>
</head>
<body>

<header class="site-header">
  <div class="brand"><span class="brand-mark"></span>Lanternfold Cybersecurity</div>
  <nav class="nav"><a class="active" href="#">Home</a><a href="#">System Solutions</a><a class="pill" href="#">Get Today</a></nav>
</header>

<section class="hero">
  <h1 class="display">CYBERSECURITY</h1>
  <p>Lorem ipsum dolor sit amet, consectetur adipiscing elit, sed do eiusmod tempor incididunt ut labore et dolore magna aliqua. Ut enim ad minim veniam, quis nostrud exercitation ullamco laboris nisi ut aliquip ex ea commodo consequat.</p>
  <div class="btn-dark">BUTTON TEXT</div>
  <div class="hero-device"><div class="hero-screen" role="img" aria-label="Close-up of a red circuit board on a laptop screen"></div></div>
  <div class="hero-base"></div>
</section>

<section class="partners">
  <div class="partner"><i></i>Terranova</div>
  <div class="partner"><i></i>Kitbridge</div>
  <div class="partner"><i></i>Notionly</div>
  <div class="partner"><i></i>Sonora</div>
  <div class="partner"><i></i>Veltaro</div>
  <div class="partner"><i></i>Terranova</div>
</section>

<section class="about">
  <div class="eyebrow">About</div>
  <h2 class="section-title display">WHO WE ARE</h2>
  <p>Lorem ipsum dolor sit amet, consectetur adipiscing elit, sed do eiusmod tempor incididunt ut labore et dolore magna aliqua. Ut enim ad minim veniam, quis nostrud exercitation ullamco laboris nisi ut aliquip ex ea commodo consequat.</p>
  <div class="learn">Learn More
    <svg width="22" height="10" viewBox="0 0 22 10"><path d="M0 5h20M16 1l4 4-4 4" fill="none" stroke="#1b1f4b" stroke-width="1.5"/></svg>
  </div>
  <div class="about-device"><div class="about-screen" role="img" aria-label="Team working on laptops around a table"></div></div>
  <div class="about-base"></div>
</section>

<section class="services">
  <div class="eyebrow">Our Services</div>
  <h2 class="section-title display">FIND SOLUTIONS</h2>
  <article class="card" style="left:124px"><small>Subtext</small><h3 class="display">HEADING</h3><p>Lorem ipsum dolor sit amet, consectetur adipiscing elit.</p><div class="btn">KNOW MORE</div></article>
  <article class="card" style="left:475px"><small>Subtext</small><h3 class="display">HEADING</h3><p>Lorem ipsum dolor sit amet, consectetur adipiscing elit.</p><div class="btn">KNOW MORE</div></article>
  <article class="card" style="left:826px"><small>Subtext</small><h3 class="display">HEADING</h3><p>Lorem ipsum dolor sit amet, consectetur adipiscing elit.</p><div class="btn">KNOW MORE</div></article>
</section>

<section class="works">
  <div class="work" style="left:-49px"><div class="frame"><div class="screen" role="img" aria-label="Coffee brand website preview" style="background:linear-gradient(90deg,#f3efe2,#6a4a2a)"></div></div><div class="base"></div></div>
  <div class="work" style="left:301px"><div class="frame"><div class="screen" role="img" aria-label="Photography studio website preview" style="background:linear-gradient(135deg,#b9b9b9,#5a5a5a)"></div></div><div class="base"></div></div>
  <div class="work" style="left:652px"><div class="frame"><div class="screen" role="img" aria-label="Black and white website preview with orange accents" style="background:linear-gradient(180deg,#2a2a2a,#6a6a6a 80%,#e25a2a 80%)"></div></div><div class="base"></div></div>
  <div class="work" style="left:1002px"><div class="frame"><div class="screen" role="img" aria-label="Coffee brand website preview" style="background:linear-gradient(90deg,#f3efe2,#6a4a2a)"></div></div><div class="base"></div></div>
  <h2 class="display">VIEW ALL OUR WORKS</h2>
  <div class="btn-outline">GO NOW</div>
</section>

<section class="clients">
  <div class="eyebrow">Know What</div>
  <h2 class="section-title display">OUR CLIENTS SAY</h2>

  <div class="quote-text" style="left:-219px">Lorem ipsum dolor sit amet, consectetur adipiscing elit, sed do eiusmod tempoar incididunt ut labore et dolore magna aliqua.</div>
  <div class="client-name" style="left:-219px">Client Name</div>

  <svg class="quote" style="left:164px" viewBox="0 0 64 50"><path d="M4 50V26L16 0h10L18 24h10v26zM36 50V26L48 0h10L50 24h10v26z" fill="#1b1f4b"/></svg>
  <div class="avatar" role="img" aria-label="Client portrait" style="left:321px;background:linear-gradient(135deg,#c9a27a,#5a4030)"></div>
  <div class="quote-text" style="left:245px">Lorem ipsum dolor sit amet, consectetur adipiscing elit, sed do eiusmod tempoar incididunt ut labore et dolore magna aliqua.</div>
  <div class="client-name" style="left:245px">Client Name</div>
  <div class="client-since" style="left:245px">Client since 2018</div>

  <svg class="quote" style="left:628px" viewBox="0 0 64 50"><path d="M4 50V26L16 0h10L18 24h10v26zM36 50V26L48 0h10L50 24h10v26z" fill="#1b1f4b"/></svg>
  <div class="avatar" role="img" aria-label="Client portrait" style="left:785px;background:linear-gradient(135deg,#d8dde3,#7a8a99)"></div>
  <div class="quote-text" style="left:709px">Lorem ipsum dolor sit amet, consectetur adipiscing elit, sed do eiusmod tempoar incididunt ut labore et dolore magna aliqua.</div>
  <div class="client-name" style="left:709px">Client Name</div>
  <div class="client-since" style="left:709px">Client since 2018</div>

  <svg class="quote" style="left:1092px" viewBox="0 0 64 50"><path d="M4 50V26L16 0h10L18 24h10v26zM36 50V26L48 0h10L50 24h10v26z" fill="#1b1f4b"/></svg>
  <div class="quote-text" style="left:1174px">Lorem ipsum dolor sit amet, consectetur adipiscing elit, sed do eiusmod tempoar incididunt ut labore et dolore magna aliqua.</div>
  <div class="client-name" style="left:1174px">Client Name</div>
  <div class="client-since" style="left:1174px">Client since 2018</div>
</section>

<section class="cta">
  <h2 class="display">READY TO BEGIN?</h2>
  <div class="field" style="left:59px">Name...</div>
  <div class="field" style="left:449px">E-mail address...</div>
  <div class="cta-btn">Let’s Go!</div>
  <div class="cta-devices" role="img" aria-label="Tablet and phone with colourful abstract artwork"></div>
</section>

<footer class="site-footer">
  <div class="brand"><span class="brand-mark"></span>Lanternfold Cybersecurity</div>
  <nav class="nav"><a class="active" href="#">Home</a><a href="#">System Solutions</a><a class="pill" href="#">Get Today</a></nav>
</footer>
<div class="copyright abs" style="left:0;width:1200px">Copyright © Year - Place Address Here</div>

</body>
</html>
```